Design für Auto-Folierung, Lieferwagen Tischlerei

Design für Lieferwagen Valbrand Kurier mit Kofferaufbau.
(Valbrand Kurier 428TXL Koffer 4325 Farbe weiß, Baujahr 2020)
Es sollte vom Design zu Holz, Möbel, Tischler, Firmenlogo passen.
Farben sollten zum Firmenlogo und der Wagenfarbe passen.
Es sollte modern und zeitlos sein.
Zusätzlicher Text und Bilder können verwendet werden.
Es würde vermutlich reichen den Aufbau und Motorhaube zu folieren, bin aber für alles offen.
Integriert werden sollte: Firmenlogo (rundum) und Anschrift (hinten) .

• Logo, Anschrift

```html
<!DOCTYPE html>
<html lang="de">
<head>
<meta charset="utf-8">
<title>Holm Tischlerei – Fahrzeugbeschriftung</title>
<link rel="stylesheet" href="https://fonts.googleapis.com/css2?family=Krona+One&display=swap">
<style>
  :root {
    --navy: #1f2a6b;
    --navy-dark: #17205a;
    --gold: #d4b64a;
    --gold-light: #f0dc86;
    --white: #ffffff;
    --stage: #f3f4f6;
    --edge: #d3d6dc;
  }
  * { margin: 0; padding: 0; box-sizing: border-box; }
  html, body { width: 1200px; height: 3305px; overflow: hidden; }
  body {
    position: relative;
    background: var(--stage);
    font-family: "Krona One", "Arial Black", sans-serif;
    color: var(--navy);
  }
  .panel { position: absolute; }
  .panel svg { position: absolute; inset: 0; width: 100%; height: 100%; }
  .abs { position: absolute; }

  /* brand mark: name set as text beside one plain square */
  .brand { position: absolute; display: flex; align-items: center; }
  .brand-square { background: var(--gold); flex: none; }
  .brand-name { color: var(--navy); line-height: 0.95; text-transform: uppercase; }
  .brand-name span { display: block; }

  .centered { left: 0; right: 0; text-align: center; }
  .white { color: var(--white); }
  .gold { color: var(--gold); }

  /* side */
  .side { left: 20px; top: 130px; width: 1160px; height: 420px; }
  .side .address { top: 306px; left: 410px; width: 750px; text-align: center; font-size: 15px; }
  .side .phone { top: 334px; left: 410px; width: 750px; text-align: center; font-size: 32px; }
  .side .web { top: 382px; left: 410px; width: 750px; text-align: center; font-size: 17px; }

  /* rear */
  .rear { left: 195px; top: 785px; width: 820px; height: 925px; }
  .rear .address { top: 420px; font-size: 40px; line-height: 53px; }
  .rear .phone { top: 690px; font-size: 58px; }
  .rear .web { top: 775px; font-size: 34px; }

  /* front */
  .cab-top { left: 250px; top: 2080px; width: 700px; height: 250px; }
  .cab-top .phone { top: 80px; font-size: 48px; }
  .cab-top .web { top: 150px; font-size: 27px; }
  .hood { left: 230px; top: 2690px; width: 740px; height: 170px; }
</style>
</head>
<body>

<section class="panel side" aria-label="Seitenansicht">
  <svg viewBox="0 0 1160 420" preserveAspectRatio="none">
    <rect x="0" y="0" width="1160" height="420" fill="var(--white)" stroke="var(--edge)"/>
    <polygon points="1160,290 410,290 290,375 0,375 0,420 1160,420" fill="var(--navy)"/>
    <polyline points="1160,290 410,290 290,375 0,375" fill="none" stroke="var(--gold)" stroke-width="7"/>
    <line x1="410" y1="0" x2="410" y2="290" stroke="var(--edge)"/>
  </svg>
  <div class="abs" role="img" aria-label="Dezentes Holzverbindungs-Muster im blauen Band" style="left:410px;top:296px;width:750px;height:124px;background:linear-gradient(90deg,var(--navy),var(--navy-dark),var(--navy));"></div>
  <div class="brand" style="left:475px;top:60px;">
    <div class="brand-square" style="width:175px;height:175px;margin-right:40px;"></div>
    <div class="brand-name"><span style="font-size:112px;">Holm</span><span style="font-size:44px;margin-top:12px;">Tischlerei</span></div>
  </div>
  <div class="brand" style="left:135px;top:315px;">
    <div class="brand-square" style="width:34px;height:34px;margin-right:8px;"></div>
    <div class="brand-name"><span style="font-size:22px;">Holm</span><span style="font-size:9px;margin-top:2px;">Tischlerei</span></div>
  </div>
  <p class="abs address white">Ahornstraße 14 · 8561 Feldau</p>
  <p class="abs phone white">+0 660 <span class="gold">5173048</span></p>
  <p class="abs web white">HOLM-TISCHLEREI.AT</p>
</section>

<section class="panel rear" aria-label="Heckansicht">
  <svg viewBox="0 0 820 925" preserveAspectRatio="none">
    <rect x="0" y="0" width="820" height="925" fill="var(--white)" stroke="var(--edge)"/>
    <rect x="0" y="635" width="820" height="290" fill="var(--navy)"/>
    <rect x="0" y="628" width="820" height="12" fill="var(--gold)"/>
  </svg>
  <div class="abs" role="img" aria-label="Dezentes Holzverbindungs-Muster im blauen Feld" style="left:0;top:640px;width:820px;height:285px;background:linear-gradient(180deg,var(--navy),var(--navy-dark));"></div>
  <div class="brand" style="left:70px;top:160px;">
    <div class="brand-square" style="width:195px;height:195px;margin-right:45px;"></div>
    <div class="brand-name"><span style="font-size:125px;">Holm</span><span style="font-size:48px;margin-top:14px;">Tischlerei</span></div>
  </div>
  <p class="abs centered address">AHORNSTRASSE 14<br>GEWERBEPARK NORD<br>8561 FELDAU</p>
  <p class="abs centered phone white">+0 660 5173048</p>
  <p class="abs centered web gold">HOLM-TISCHLEREI.AT</p>
</section>

<section class="panel cab-top" aria-label="Frontaufbau">
  <svg viewBox="0 0 700 250" preserveAspectRatio="none">
    <rect x="0" y="0" width="700" height="250" fill="var(--white)" stroke="var(--edge)"/>
  </svg>
  <p class="abs centered phone">+0 660 5173048</p>
  <p class="abs centered web">HOLM-TISCHLEREI.AT</p>
</section>

<section class="panel hood" aria-label="Motorhaube">
  <svg viewBox="0 0 740 170" preserveAspectRatio="none">
    <rect x="0" y="0" width="740" height="170" fill="var(--white)" stroke="var(--edge)"/>
  </svg>
  <div class="brand" style="left:165px;top:42px;">
    <div class="brand-square" style="width:86px;height:86px;margin-right:24px;"></div>
    <div class="brand-name"><span style="font-size:58px;">Holm</span><span style="font-size:22px;margin-top:6px;">Tischlerei</span></div>
  </div>
</section>

</body>
</html>
```